Business card design for Plumbing and Gas fitting company

We need a business card design for our plumbing and gas fitting company using the company logo and director details. Design should be modern and eye-catching however kept reasonably simple. This design should be targeted at commercial businesses/work so professionalism is key.

Target Market(s)

Commercial/business

Industry/Entity Type

Plumbing

Contact Information for Business Card

Warren Dohey
Director
027 581 9043
warren@vantorplumbingandgas.example
PO Box 7816
Palmerston North 4472

Font styles to use
Sans Serif

Requirements
Must have
• Logo
• Modern
• Kept simple
Nice to have
• Colour scheme based around logo

```html
<!DOCTYPE html>
<html lang="en">
<head>
<meta charset="utf-8">
<title>Vantor Plumbing &amp; Gas – Business Card</title>
<link rel="stylesheet" href="https://fonts.googleapis.com/css2?family=Nunito:wght@400;600;700;800&display=swap">
<style>
  :root {
    --stage: #ecebef;
    --card: #ffffff;
    --blue: #1c8ed6;
    --orange: #f39a4f;
    --peach: #fdd6b6;
    --peach-text: #f2a366;
    --shadow: rgba(40, 30, 60, 0.16);
  }
  * { box-sizing: border-box; margin: 0; padding: 0; }
  html, body { width: 1200px; height: 800px; overflow: hidden; }
  body {
    background: var(--stage);
    font-family: "Nunito", sans-serif;
    display: flex;
    align-items: center;
    justify-content: center;
    gap: 60px;
  }
  .card {
    position: relative;
    width: 530px;
    height: 310px;
    background: var(--card);
    border-radius: 40px;
    box-shadow: 0 14px 36px var(--shadow);
    overflow: hidden;
  }

  /* Front */
  .card--front {
    display: flex;
    align-items: center;
    justify-content: center;
    gap: 16px;
  }
  .brand-name {
    color: var(--blue);
    font-weight: 800;
    font-size: 34px;
    letter-spacing: 0.2px;
  }
  .brand-dot {
    width: 34px;
    height: 34px;
    border-radius: 50%;
    background: var(--orange);
    flex: none;
  }

  /* Back */
  .name-tab {
    position: absolute;
    left: 0;
    top: 0;
    width: 300px;
    height: 96px;
    background: var(--peach);
    border-radius: 0 0 26px 0;
    padding: 20px 0 0 44px;
  }
  .name-tab__name {
    color: var(--peach-text);
    font-weight: 700;
    font-size: 27px;
    line-height: 1.1;
  }
  .name-tab__role {
    color: var(--peach-text);
    font-weight: 600;
    font-style: italic;
    font-size: 15px;
    margin-top: 2px;
  }
  .back-mark {
    position: absolute;
    left: 44px;
    top: 114px;
    display: flex;
    align-items: center;
    gap: 10px;
  }
  .back-mark__dot {
    width: 22px;
    height: 22px;
    border-radius: 50%;
    background: var(--orange);
  }
  .back-mark__name {
    color: var(--blue);
    font-weight: 800;
    font-size: 16px;
  }
  .contact {
    position: absolute;
    right: 34px;
    bottom: 32px;
    list-style: none;
    display: flex;
    flex-direction: column;
    align-items: flex-end;
    gap: 14px;
  }
  .contact__item {
    display: flex;
    align-items: center;
    gap: 12px;
    color: var(--blue);
    font-weight: 600;
    font-size: 14px;
    text-align: right;
    line-height: 1.25;
  }
  .contact__icon {
    width: 30px;
    height: 30px;
    border-radius: 50%;
    background: var(--blue);
    display: flex;
    align-items: center;
    justify-content: center;
    flex: none;
  }
  .contact__icon svg { width: 16px; height: 16px; }
</style>
</head>
<body>

  <section class="card card--front" aria-label="Business card front">
    <span class="brand-dot" aria-hidden="true"></span>
    <span class="brand-name">Vantor Plumbing &amp; Gas</span>
  </section>

  <section class="card card--back" aria-label="Business card back">
    <div class="name-tab">
      <p class="name-tab__name">Warren Dohey</p>
      <p class="name-tab__role">Director</p>
    </div>

    <div class="back-mark">
      <span class="back-mark__dot" aria-hidden="true"></span>
      <span class="back-mark__name">Vantor Plumbing &amp; Gas</span>
    </div>

    <ul class="contact">
      <li class="contact__item">
        <span>warren@vantorplumbingandgas.example</span>
        <span class="contact__icon" aria-hidden="true">
          <svg viewBox="0 0 16 16"><rect x="2" y="4" width="12" height="8" rx="1" fill="#fff"/><path d="M2.5 4.5 8 9l5.5-4.5" fill="none" stroke="#1c8ed6" stroke-width="1.2"/></svg>
        </span>
      </li>
      <li class="contact__item">
        <span>027 581 9043</span>
        <span class="contact__icon" aria-hidden="true">
          <svg viewBox="0 0 16 16"><path d="M4.5 2.5c.6-.4 1.3-.2 1.6.4l.9 1.8c.2.5.1 1-.3 1.3l-.8.6c.6 1.3 1.6 2.3 2.9 2.9l.6-.8c.3-.4.8-.5 1.3-.3l1.8.9c.6.3.8 1 .4 1.6l-.6.9c-.5.7-1.4 1-2.2.7C6.9 11.5 4.5 9.1 3.5 6.3c-.3-.8 0-1.7.7-2.2z" fill="#fff"/></svg>
        </span>
      </li>
      <li class="contact__item">
        <span>PO Box 7816<br>Palmerston North 4472</span>
        <span class="contact__icon" aria-hidden="true">
          <svg viewBox="0 0 16 16"><path d="M8 2.5 2 7.5h1.8V13h3V10h2.4v3h3V7.5H14z" fill="#fff"/></svg>
        </span>
      </li>
    </ul>
  </section>

</body>
</html>
```